Clinical psychologist - Psychotherapist business card

Hi everyone, I'm a clinical psychologist and psychotherapist, and I’m looking for a logo for my business card. The front will feature only the logo, while the back will include my contact details (and possibly a subtle touch of the logo). I've found two logos that I like, but the first one feels a bit childish—it lacks professionalism and doesn’t stand out from other similar designs. The second one, which I do like, unfortunately gives off a clinical, impersonal vibe.

Feel free to improvise—you don’t need to base the design on the logos I previously mentioned.

I generally prefer minimalistic designs that convey warmth, trust, and professionalism. I’d also like the card to have a bright background to make it feel inviting.

Additionally, I’m leaning toward using letterpress for the print technique, so the design should be compatible with that style—elegant, tactile, and clean. However, I’m still open to other options if they better suit the design.

UPDATE: I'm considering naming my business “Kalydo” (top-level domain: .gr), so you could incorporate that as well.

Target Market(s)

Psychology clients, Psychiatrists, Social media users

Industry/Entity Type

Clinical psychologist - Psychotherapist

Contact Information for Business Card

To be added later on

Colors

Designer to choose colors to be used in the design.

Requirements
Nice to have
• Possibly my initials on the front side. They are Δ Μ (capital letters) or δ μ (small letters).
Should not have
• Portraits of famous psychologists

```html
<!DOCTYPE html>
<html lang="en">
<head>
<meta charset="utf-8">
<title>Kalydo – Business Card</title>
<link href="https://fonts.googleapis.com/css2?family=Playfair+Display:wght@700&family=Poppins:wght@400;500&display=swap" rel="stylesheet">
<style>
  :root {
    --page: #dedede;
    --paper: #ffffff;
    --blue: #93cfe5;
    --blue-light: #e3f2f8;
    --ink: #111111;
  }
  * { margin: 0; padding: 0; box-sizing: border-box; }
  html, body { width: 1200px; height: 1005px; overflow: hidden; background: var(--page); }
  .card {
    position: absolute; left: 250px; width: 700px; height: 400px;
    background: var(--paper); overflow: hidden;
    box-shadow: 4px 5px 8px rgba(0,0,0,0.28);
    font-family: "Poppins", sans-serif; color: var(--ink);
  }
  .card--front { top: 75px; }
  .card--back { top: 528px; }
  .card__art { position: absolute; inset: 0; width: 700px; height: 400px; }
  .brand {
    position: absolute; font-family: "Playfair Display", serif; font-weight: 700;
    color: var(--ink); line-height: 1; display: flex; align-items: center; gap: 12px;
  }
  .brand__dot { display: inline-block; border-radius: 50%; background: var(--blue); }
  .card--front .brand { left: 55px; top: 112px; font-size: 44px; }
  .card--front .brand__dot { width: 20px; height: 20px; }
  .card--back .brand { left: 0; right: 0; top: 190px; justify-content: center; font-size: 52px; }
  .card--back .brand__dot { width: 22px; height: 22px; }
  .person { position: absolute; left: 311px; top: 44px; }
  .person__name { font-family: "Playfair Display", serif; font-weight: 700; font-size: 42px; line-height: 1; letter-spacing: 0.5px; }
  .person__name span { color: var(--blue); }
  .person__role { margin-top: 13px; font-size: 12.5px; letter-spacing: 2.6px; font-weight: 500; }
  .contacts { position: absolute; left: 306px; top: 155px; list-style: none; }
  .contacts li { display: flex; align-items: center; height: 40px; font-size: 15.5px; }
  .contacts svg { width: 32px; height: 32px; margin-right: 11px; flex: none; }
  .web { position: absolute; font-size: 21px; letter-spacing: 4.2px; font-weight: 500; white-space: nowrap; }
  .web span { color: #ffffff; }
  .card--front .web { left: 368px; top: 338px; }
  .card--back .web { left: 0; right: 0; top: 325px; text-align: center; }
  .card--back .web span { color: var(--blue); }
</style>
</head>
<body>

<section class="card card--front" aria-label="Card front">
  <svg class="card__art" viewBox="0 0 700 400" role="img" aria-label="Soft blue abstract background shapes">
    <defs>
      <radialGradient id="front-corner" cx="0" cy="1" r="1">
        <stop offset="0" stop-color="#93cfe5"/>
        <stop offset="0.55" stop-color="#c4e5f1"/>
        <stop offset="1" stop-color="#ffffff" stop-opacity="0"/>
      </radialGradient>
    </defs>
    <rect x="0" y="150" width="330" height="250" fill="url(#front-corner)"/>
    <path fill="var(--blue)" d="M0 330 C120 300 200 290 317 295 C410 300 460 322 530 316 C610 308 660 288 700 265 L700 400 L0 400 Z"/>
  </svg>

  <div class="brand"><span class="brand__dot"></span>Kalydo</div>

  <div class="person">
    <h1 class="person__name">Daniel <span>Moreau</span></h1>
    <p class="person__role">CLINICAL PSYCHOLOGIST</p>
  </div>

  <ul class="contacts">
    <li>
      <svg viewBox="0 0 32 32" aria-hidden="true"><circle cx="16" cy="16" r="16" fill="var(--blue)"/><path d="M16 8a5.5 5.5 0 0 0-5.5 5.5C10.5 18 16 24 16 24s5.5-6 5.5-10.5A5.5 5.5 0 0 0 16 8zm0 7.5a2 2 0 1 1 0-4 2 2 0 0 1 0 4z" fill="var(--ink)"/></svg>
      22 Harbor Lane, Suite 5, Athens 10558
    </li>
    <li>
      <svg viewBox="0 0 32 32" aria-hidden="true"><circle cx="16" cy="16" r="16" fill="var(--blue)"/><path d="M11.5 9.5l2.5-.5 1.5 3.5-1.7 1.2a8 8 0 0 0 3.5 3.5l1.2-1.7 3.5 1.5-.5 2.5c-.3 1-1.3 1.5-2.3 1.3-4.5-1-8-4.5-9-9-.2-1 .3-2 1.3-2.3z" fill="var(--ink)"/></svg>
      555 0142 376
    </li>
    <li>
      <svg viewBox="0 0 32 32" aria-hidden="true"><circle cx="16" cy="16" r="16" fill="var(--blue)"/><rect x="10" y="11.5" width="12" height="9" fill="var(--ink)"/><path d="M10 11.5l6 5 6-5" fill="none" stroke="var(--blue)" stroke-width="1.2"/></svg>
      info@kalydo.gr
    </li>
  </ul>

  <p class="web">www.<span>kalydo</span>.gr.com</p>
</section>

<section class="card card--back" aria-label="Card back">
  <svg class="card__art" viewBox="0 0 700 400" role="img" aria-label="Soft blue abstract corner shapes">
    <defs>
      <radialGradient id="back-top" cx="0" cy="0" r="1">
        <stop offset="0" stop-color="#93cfe5"/>
        <stop offset="0.5" stop-color="#c4e5f1"/>
        <stop offset="1" stop-color="#ffffff" stop-opacity="0"/>
      </radialGradient>
      <radialGradient id="back-bottom" cx="1" cy="1" r="1">
        <stop offset="0" stop-color="#93cfe5"/>
        <stop offset="0.5" stop-color="#c4e5f1"/>
        <stop offset="1" stop-color="#ffffff" stop-opacity="0"/>
      </radialGradient>
    </defs>
    <rect x="0" y="0" width="300" height="260" fill="url(#back-top)"/>
    <rect x="420" y="100" width="280" height="300" fill="url(#back-bottom)"/>
  </svg>

  <div class="brand"><span class="brand__dot"></span>Kalydo</div>

  <p class="web">www.<span>kalydo</span>.gr.com</p>
</section>

</body>
</html>
```